Brightwell Chilled Supplies Stationery Design

Stationery Design

Thank you to all those who have submitted the logos. We have selected the logo for our new identity and we are now looking for stationery ideas.

The attached logo must be used in all stationery designs.

We require the following items of stationery:

1. Business Cards for 10 employees – Double Sided – All the card will have the same address:

7 – 31 Marlowby Lane, Kingston Upon Thames, Surrey, KT9 3QX, United Kingdom

Office phone number: +44 (0)208 631 7094

Freephone: 0800 113 4927

Fax: +44 (0)20 8392 6481

Website: www.brightwellchilled.example

The names on the cards and mobile numbers – will be given on selection of final design.

A few of the cards will have different emails but 5/6 card will have the same email address.

2. Letterhead A4 – same contact details as above – email address to be used info@brightwellchilled.example

3. Compliments Slip – same details as no.2

4. Envelope designs – with just the address, Freephone and Website.

Sizes Required: C4 – 324mm x 229mm – Windows and Regular

DL – 110mm x 220mm – Windows and Regular

5. A4 Ring Binder – Logo at the front and back and side; company name on the front and side of the binder (Brightwell Chilled Supplies); contact details at the back; same as number 2 above.

The ring binder will have food, drink and hygiene inserts inside and will act as a temporary brochure.

It may help with the design process to know we sell a range of frozen food products including chips, burgers, fish, frozen poultry items, vegetables, ice cream, desserts, bakery products, pies, pasties, onion rings, pizza toppings etc.

We also sell ambient products such as sauces, crisps such as dunmores, chocolates such as Threlfalls, Vorreau, Pell etc.

Drinks wise we sell branded products such as zesta fizz, korvo, brisa, glint, blue heron etc; As well as juices and mineral water.

We also sell hygiene products such as tissue paper, hand towels, and other washroom products, bleaches etc.

Our website doesn’t have the full range of products but gives you a good idea of what we do www.brightwellchilled.example

Please note we are looking for a classy, slick design so don’t worry about trying to add all the products on the binder design; these have just been given to assist with the design process.

We may add a slogan to the stationery but the final decision on this still has to be taken and the profile will be updated within the next 72 hours.

This project will only last a maximum of 10-14 days, we don’t want to drag it out like the logo so please only submit creative ideas; which have been given thought in terms of design, text and graphics.

Any questions, feel free to ask.

Thank you and we look forward to your designs.

Regards

Tariq Benmore

UPDATED FILES ATTACHED

I've uploaded an Adobe Illustrator CS2.ai file, and an EPS file of my new logo so you can get better clarity within your designs for this project

Thanks
Tariq

Hi

We have had various questions in respect of dimensions and budget; we have addressed both issues below by providing dimensions and we will be increasing the budget to $500 as soon as Sketch Hive let us know how we can increase; they have already been emailed.

In respect of the dimensions, we have had various answers but here are the most common sizes.

 

There are various sizes of lever arch A4 folders but the most common ones are below:

 

 

• Dimensions width 28.5cm, height 32cm,spine 9cm
• Dimensions (mm)H:315 x W:285
• Dimensions (mm) H:31cm x W:27cm

 

The most common thickness in the UK seems to be 70mm; so can we use this as a guide please.

 

 

Compliment Slip Sizes:

 

• Our Compliment Slips are DL in size. You should design your Compliment Slip to DL dimension but also add a 3mm bleed around each edge.

 

Trim Size – 99mm x 210mm

 

With Bleed – 105mm – 216mm

 

 

Business Cards:

 

Trim Size: 85mm x 55mm

 

With Bleed: 91mm x 61mm

 

 

We have extended the time frame and the budget on this so look forward to new designs.

 

I hope this helps and all the best for Christmas and 2010..

 

Regards

Tariq Benmore.

Hi Guys

Another important point to mention as each country has different rules...

In the Uk the postage stamps go in the top right hand corner of the envelope so we will have to have our logo company details etc in either the top left or the bottom of the envelope.

Also all envelopes must have at the back our return address:

Return Address:

Brightwell Chilled Supplies Ltd
7 - 31 Marlowby Lane
Kingston Upon Thames
Surrey
KT9 3QX

So we could even have the business logo, name and website address at the front and the address at the back.

Regards

Tariq

```html
<!DOCTYPE html>
<html lang="en">
<head>
<meta charset="utf-8">
<title>Brightwell Chilled Supplies – Stationery Set</title>
<link href="https://fonts.googleapis.com/css2?family=Source+Sans+3:wght@400;600;700&display=swap" rel="stylesheet">
<style>
  :root {
    --backdrop: #262b2c;
    --brand-red: #8b181d;
    --brand-navy: #35346b;
    --paper: #ffffff;
    --ink: #1e1e24;
    --ink-soft: #8a8a90;
    --window-grey: #cfcfcf;
    --watermark: #ebe6ef;
  }
  * { box-sizing: border-box; margin: 0; padding: 0; }
  html, body { width: 1200px; height: 934px; overflow: hidden; }
  body {
    position: relative;
    background: var(--backdrop);
    font-family: "Source Sans 3", sans-serif;
    color: var(--ink);
  }
  .item { position: absolute; background: transparent; }
  .item > svg.shape { position: absolute; inset: 0; width: 100%; height: 100%; display: block; }
  .item > * { position: absolute; }

  .brand { display: flex; align-items: center; gap: 3px; font-weight: 700; color: var(--ink); white-space: nowrap; line-height: 1; }
  .brand .dot { width: 0.9em; height: 0.9em; border-radius: 50%; background: var(--brand-red); flex: none; }
  .brand.light { color: var(--paper); }
  .brand.light .dot { background: var(--paper); }

  .flap-name { color: var(--paper); font-weight: 700; font-size: 7px; letter-spacing: 0.5px; transform: translateX(-50%); white-space: nowrap; }

  .address { color: var(--ink-soft); line-height: 1.3; white-space: nowrap; }
  .address b { font-weight: 700; }
  .address.right { text-align: right; }

  .window { background: var(--window-grey); border-radius: 5px; }

  /* Envelopes */
  .env-c4 { width: 287px; height: 438px; }
  .env-c4 .brand { left: 13px; top: 52px; font-size: 9px; }
  .env-c4 .address { left: 25px; top: 398px; font-size: 3.8px; }
  .env-dl { width: 276px; height: 168px; }
  .env-dl .brand { left: 8px; top: 47px; font-size: 9px; }
  .env-dl .address { left: 8px; top: 136px; font-size: 3.8px; }

  /* Letterhead */
  .letterhead { left: 919px; top: 27px; width: 271px; height: 380px; background: var(--paper); }
  .letterhead .brand { left: 11px; top: 12px; font-size: 9px; }
  .letterhead .rule { left: 85px; top: 26px; width: 180px; height: 0.5px; background: var(--ink-soft); }
  .letterhead .tagline { right: 6px; top: 21px; font-size: 2.8px; color: var(--ink-soft); letter-spacing: 0.1px; }
  .letterhead .address { right: 6px; top: 29px; font-size: 2.8px; }
  .letterhead .watermark { left: 40px; top: 170px; width: 190px; text-align: center; color: var(--watermark); font-weight: 700; font-size: 30px; line-height: 1; }
  .letterhead .site { left: 0; width: 100%; top: 368px; text-align: center; color: var(--paper); font-size: 4px; font-weight: 600; }

  /* Business cards */
  .card-back { left: 623px; top: 413px; width: 114px; height: 76px; background: var(--brand-red); }
  .card-back .brand { left: 50%; top: 50%; transform: translate(-50%, -50%); font-size: 8px; }
  .card-front { left: 762px; top: 411px; width: 114px; height: 76px; background: var(--paper); }
  .card-front .brand { right: 8px; top: 9px; font-size: 5.5px; }
  .card-front .person { left: 6px; top: 33px; width: 44px; text-align: center; }
  .card-front .person .name { font-size: 5px; font-weight: 700; display: block; }
  .card-front .person .role { font-size: 2.6px; font-weight: 700; display: block; }
  .card-front .address { right: 8px; top: 31px; font-size: 2.6px; }

  /* Ring binder */
  .binder { left: 21px; top: 501px; width: 827px; height: 394px; overflow: hidden; }
  .binder .cover-title { left: 0; width: 413px; margin-left: 206px; top: 62px; text-align: center; color: var(--paper); }
  .binder .cover-title .word { display: block; font-weight: 700; font-size: 30px; line-height: 1; }
  .binder .cover-title .sub { display: block; font-weight: 700; font-size: 7px; letter-spacing: 2.5px; margin-top: 5px; }
  .binder .spine-brand { left: 18px; top: 353px; font-size: 14px; }
  .binder .address { right: 477px; top: 342px; font-size: 5.3px; color: var(--paper); }
  .binder .back-brand { left: 592px; top: 328px; font-size: 17px; }

  /* Compliments slip */
  .comp-slip { left: 885px; top: 509px; width: 271px; height: 131px; }
  .comp-slip .heading { left: 13px; top: 15px; font-size: 4.6px; font-weight: 700; }
  .comp-slip .brand { right: 10px; top: 14px; font-size: 7.5px; }
  .comp-slip .address { right: 9px; top: 75px; font-size: 2.8px; }
  .comp-slip .site { left: 0; width: 100%; top: 121px; text-align: center; color: var(--paper); font-size: 3.8px; font-weight: 600; }
</style>
</head>
<body>

<!-- C4 envelope, regular -->
<section class="item env-c4" style="left:18px; top:13px;" aria-label="C4 envelope">
  <svg class="shape" viewBox="0 0 287 438" aria-hidden="true">
    <rect y="31" width="287" height="407" fill="var(--paper)"/>
    <path d="M0,31 L37,0 L251,0 L287,31 L287,91 Q156,35 0,31Z" fill="var(--brand-red)"/>
    <path d="M0,31 Q156,35 287,91 L287,105 Q156,44 0,31Z" fill="var(--brand-navy)"/>
  </svg>
  <span class="flap-name" style="left:144px; top:10px;">Brightwell</span>
  <div class="brand"><span class="dot"></span>Brightwell Chilled Supplies</div>
  <p class="address"><b>Address:</b> 7 – 31 Marlowby Lane,<br>Kingston Upon Thames, Surrey,<br>KT9 3QX, United Kingdom<br><b>Freephone:</b> 0800 113 4927<br><b>Web:</b> www.brightwellchilled.example</p>
</section>

<!-- C4 envelope, window -->
<section class="item env-c4" style="left:316px; top:13px;" aria-label="C4 window envelope">
  <svg class="shape" viewBox="0 0 287 438" aria-hidden="true">
    <rect y="31" width="287" height="407" fill="var(--paper)"/>
    <path d="M0,31 L37,0 L251,0 L287,31 L287,91 Q156,35 0,31Z" fill="var(--brand-red)"/>
    <path d="M0,31 Q156,35 287,91 L287,105 Q156,44 0,31Z" fill="var(--brand-navy)"/>
  </svg>
  <span class="flap-name" style="left:144px; top:10px;">Brightwell</span>
  <div class="brand"><span class="dot"></span>Brightwell Chilled Supplies</div>
  <div class="window" style="left:25px; top:99px; width:129px; height:51px;"></div>
  <p class="address"><b>Address:</b> 7 – 31 Marlowby Lane,<br>Kingston Upon Thames, Surrey,<br>KT9 3QX, United Kingdom<br><b>Freephone:</b> 0800 113 4927<br><b>Web:</b> www.brightwellchilled.example</p>
</section>

<!-- DL envelope, regular -->
<section class="item env-dl" style="left:620px; top:21px;" aria-label="DL envelope">
  <svg class="shape" viewBox="0 0 276 168" aria-hidden="true">
    <rect y="31" width="276" height="137" fill="var(--paper)"/>
    <path d="M0,31 L37,0 L240,0 L276,31 L276,86 Q150,38 0,31Z" fill="var(--brand-red)"/>
    <path d="M0,31 Q150,38 276,86 L276,100 Q150,47 0,31Z" fill="var(--brand-navy)"/>
  </svg>
  <span class="flap-name" style="left:140px; top:10px;">Brightwell</span>
  <div class="brand"><span class="dot"></span>Brightwell Chilled Supplies</div>
  <p class="address"><b>Address:</b> 7 – 31 Marlowby Lane,<br>Kingston Upon Thames, Surrey,<br>KT9 3QX, United Kingdom<br><b>Freephone:</b> 0800 113 4927<br><b>Web:</b> www.brightwellchilled.example</p>
</section>

<!-- DL envelope, window -->
<section class="item env-dl" style="left:619px; top:217px;" aria-label="DL window envelope">
  <svg class="shape" viewBox="0 0 276 168" aria-hidden="true">
    <rect y="31" width="276" height="137" fill="var(--paper)"/>
    <path d="M0,31 L37,0 L240,0 L276,31 L276,86 Q150,38 0,31Z" fill="var(--brand-red)"/>
    <path d="M0,31 Q150,38 276,86 L276,100 Q150,47 0,31Z" fill="var(--brand-navy)"/>
  </svg>
  <span class="flap-name" style="left:140px; top:10px;">Brightwell</span>
  <div class="brand"><span class="dot"></span>Brightwell Chilled Supplies</div>
  <div class="window" style="left:143px; top:101px; width:113px; height:45px;"></div>
  <p class="address"><b>Address:</b> 7 – 31 Marlowby Lane,<br>Kingston Upon Thames, Surrey,<br>KT9 3QX, United Kingdom<br><b>Freephone:</b> 0800 113 4927<br><b>Web:</b> www.brightwellchilled.example</p>
</section>

<!-- A4 letterhead -->
<section class="item letterhead" aria-label="A4 letterhead">
  <svg class="shape" viewBox="0 0 271 380" aria-hidden="true">
    <path d="M0,350 Q136,368 271,350 L271,380 L0,380Z" fill="var(--brand-red)"/>
    <path d="M0,346 Q136,362 271,345 L271,350 Q136,368 0,350Z" fill="var(--brand-navy)"/>
  </svg>
  <div class="brand"><span class="dot"></span>Brightwell Chilled Supplies</div>
  <div class="rule"></div>
  <p class="tagline">YOUR TAGLINE HERE &nbsp; YOUR TAGLINE HERE &nbsp; YOUR TAGLINE HERE</p>
  <p class="address right">7 – 31 Marlowby Lane, Kingston Upon Thames,<br>Surrey, KT9 3QX, United Kingdom<br><b>Office Phone:</b> +44 (0)208 631 7094<br><b>Freephone:</b> 0800 113 4927<br><b>Fax:</b> +44 (0)20 8392 6481<br><b>Email:</b> info@brightwellchilled.example<br><b>Web:</b> www.brightwellchilled.example</p>
  <p class="watermark">Brightwell</p>
  <p class="site">www.brightwellchilled.example</p>
</section>

<!-- Business card, back -->
<section class="item card-back" aria-label="Business card back">
  <div class="brand light"><span class="dot"></span>Brightwell</div>
</section>

<!-- Business card, front -->
<section class="item card-front" aria-label="Business card front">
  <div class="brand"><span class="dot"></span>Brightwell Chilled Supplies</div>
  <p class="person"><span class="name">John Doe</span><span class="role">Manager</span></p>
  <p class="address right">7 – 31 Marlowby Lane,<br>Kingston Upon Thames, Surrey,<br>KT9 3QX, United Kingdom<br><b>Office Phone:</b> +44 (0)208 631 7094<br><b>Mobile Phone:</b> 0744 210 386<br><b>Fax:</b> +44 (0)20 8392 6481<br><b>Email:</b> j.doe@brightwellchilled.example<br><b>Web:</b> www.brightwellchilled.example</p>
</section>

<!-- A4 ring binder, open flat -->
<section class="item binder" aria-label="A4 ring binder cover">
  <svg class="shape" viewBox="0 0 827 394" aria-hidden="true">
    <rect width="827" height="394" fill="var(--brand-red)"/>
    <path d="M455,394 Q590,150 827,110 L827,131 Q600,172 470,394Z" fill="var(--brand-navy)"/>
    <path d="M470,394 Q600,172 827,131 L827,394Z" fill="var(--paper)"/>
  </svg>
  <div class="cover-title">
    <span class="word">Brightwell</span>
    <span class="sub">CHILLED SUPPLIES</span>
  </div>
  <div class="brand light spine-brand"><span class="dot"></span>Brightwell</div>
  <p class="address right">7 – 31 Marlowby Lane, Kingston Upon Thames,<br>Surrey, KT9 3QX, United Kingdom<br><b>Office Phone:</b> +44 (0)208 631 7094<br><b>Freephone:</b> 0800 113 4927<br><b>Fax:</b> +44 (0)20 8392 6481<br><b>Email:</b> info@brightwellchilled.example<br><b>Web:</b> www.brightwellchilled.example</p>
  <div class="brand back-brand"><span class="dot"></span>Brightwell Chilled</div>
</section>

<!-- Compliments slip -->
<section class="item comp-slip" aria-label="Compliments slip">
  <svg class="shape" viewBox="0 0 271 131" aria-hidden="true">
    <rect width="271" height="131" fill="var(--paper)"/>
    <path d="M0,106 Q136,122 271,106 L271,131 L0,131Z" fill="var(--brand-red)"/>
    <path d="M0,101 Q136,116 271,100 L271,106 Q136,122 0,106Z" fill="var(--brand-navy)"/>
  </svg>
  <p class="heading">WITH COMPLIMENTS</p>
  <div class="brand"><span class="dot"></span>Brightwell Chilled Supplies</div>
  <p class="address right">7 – 31 Marlowby Lane, Kingston Upon Thames,<br>Surrey, KT9 3QX, United Kingdom<br><b>Office Phone:</b> +44 (0)208 631 7094<br><b>Freephone:</b> 0800 113 4927<br><b>Fax:</b> +44 (0)20 8392 6481<br><b>Email:</b> info@brightwellchilled.example<br><b>Web:</b> www.brightwellchilled.example</p>
  <p class="site">www.brightwellchilled.example</p>
</section>

</body>
</html>
```